Legal Stationary

A full set of stationery is required
The image and logo, along with colour, are set and attached.
The style should be modern, clean, and corporate. Not just a basic template off the web.
In addition to the address/website/email/phone fields for DX and KWT number, with the text “the firm is authorised and regulated by the KWT”
All files in all formats will be needed to allow editing after. Initial setup of templates will be required, and details for 4 business cards will be supplied.
Target Market(s)
Consumers of legal services
Industry/Entity Type
Legal

```html
<!DOCTYPE html>
<html lang="en">
<head>
<meta charset="utf-8">
<title>Brennan Law – Stationery Set</title>
<link href="https://fonts.googleapis.com/css2?family=Roboto:wght@400;500&display=swap" rel="stylesheet">
<style>
  :root {
    --backdrop: #7b7b7b;
    --brand-blue: #233b93;
    --paper: #ffffff;
    --ink-light: #ffffff;
    --shadow: rgba(0, 0, 0, 0.35);
  }
  * { margin: 0; padding: 0; box-sizing: border-box; }
  html, body {
    width: 1199px; height: 1200px; overflow: hidden;
    background: var(--backdrop);
    font-family: "Roboto", Arial, sans-serif;
  }
  .canvas { position: relative; width: 1199px; height: 1200px; }
  .sheet {
    position: absolute;
    background: var(--paper);
    box-shadow: 6px 8px 14px var(--shadow);
  }
  .wordmark {
    position: absolute;
    display: flex; align-items: center; gap: 10px;
    font-weight: 500; color: var(--brand-blue);
    letter-spacing: 0.5px; white-space: nowrap;
  }
  .wordmark .mark-square {
    display: block; background: var(--brand-blue);
  }
  .wordmark.on-blue { color: var(--ink-light); }
  .wordmark.on-blue .mark-square { background: var(--ink-light); }

  /* Letterhead */
  .letterhead { left: 221px; top: 62px; width: 758px; height: 1072px; }
  .letterhead .wordmark { left: 50%; top: 120px; transform: translateX(-50%); font-size: 32px; }
  .letterhead .wordmark .mark-square { width: 22px; height: 22px; }
  .footer-band { position: absolute; left: 0; }
  .letterhead .footer-band { top: 972px; width: 758px; height: 80px; }

  .contact {
    position: absolute; color: var(--ink-light);
    display: flex; flex-direction: column;
  }
  .contact .row { display: flex; align-items: center; }
  .contact svg { flex: none; }

  .letterhead .contact { font-size: 16px; line-height: 22px; }
  .letterhead .contact.left { left: 54px; top: 1001px; }
  .letterhead .contact.left svg { width: 12px; height: 12px; margin-right: 9px; }
  .letterhead .contact.right { left: 528px; top: 1001px; }
  .letterhead .contact.right .row { align-items: flex-start; }
  .letterhead .contact.right svg { width: 11px; height: 14px; margin: 4px 7px 0 0; }

  /* Business card front */
  .card-front { left: 50px; top: 199px; width: 411px; height: 240px; background: var(--brand-blue); }
  .card-front .wordmark { left: 50%; top: 42px; transform: translateX(-50%); font-size: 30px; }
  .card-front .wordmark .mark-square { width: 20px; height: 20px; }
  .card-front .person {
    position: absolute; left: 0; width: 100%; top: 131px; text-align: center;
    color: var(--ink-light); font-size: 18px; font-weight: 500;
  }
  .card-front .person .role { font-size: 11px; font-weight: 400; }
  .card-front .contact { font-size: 11.5px; line-height: 16px; }
  .card-front .contact.left { left: 30px; top: 179px; }
  .card-front .contact.left svg { width: 8px; height: 8px; margin-right: 8px; }
  .card-front .contact.right { left: 237px; top: 179px; }
  .card-front .contact.right .row { align-items: flex-start; }
  .card-front .contact.right svg { width: 7px; height: 10px; margin: 3px 8px 0 0; }

  /* Business card back */
  .card-back { left: 50px; top: 462px; width: 411px; height: 239px; }
  .card-back .wordmark { left: 50%; top: 95px; transform: translateX(-50%); font-size: 40px; }
  .card-back .wordmark .mark-square { width: 28px; height: 28px; }

  /* Envelope */
  .envelope { left: 483px; top: 649px; width: 676px; height: 338px; }
  .envelope .wordmark { left: 81px; top: 50px; font-size: 30px; }
  .envelope .wordmark .mark-square { width: 20px; height: 20px; }
  .envelope .footer-band { top: 255px; width: 676px; height: 70px; }
  .envelope .contact { font-size: 14px; line-height: 19px; }
  .envelope .contact.left { left: 64px; top: 281px; }
  .envelope .contact.left svg { width: 9px; height: 9px; margin-right: 7px; }
  .envelope .contact.right { left: 466px; top: 281px; }
  .envelope .contact.right .row { align-items: flex-start; }
  .envelope .contact.right svg { width: 8px; height: 11px; margin: 3px 7px 0 0; }
</style>
</head>
<body>
<svg width="0" height="0" style="position:absolute">
  <defs>
    <symbol id="icon-phone" viewBox="0 0 24 24"><path fill="currentColor" d="M6.6 10.8a15.1 15.1 0 0 0 6.6 6.6l2.2-2.2c.3-.3.7-.4 1-.2 1.1.4 2.3.6 3.6.6.6 0 1 .4 1 1V20c0 .6-.4 1-1 1A17 17 0 0 1 3 4c0-.6.4-1 1-1h3.5c.6 0 1 .4 1 1 0 1.3.2 2.5.6 3.6.1.3 0 .7-.2 1z"/></symbol>
    <symbol id="icon-mail" viewBox="0 0 24 24"><path fill="currentColor" d="M2 5h20v14H2z M2 5l10 7 10-7" /><path fill="none" stroke="#233b93" stroke-width="2" d="M2 6l10 7 10-7"/></symbol>
    <symbol id="icon-pin" viewBox="0 0 16 22"><path fill="currentColor" d="M8 0a8 8 0 0 0-8 8c0 6 8 14 8 14s8-8 8-14a8 8 0 0 0-8-8zm0 11a3 3 0 1 1 0-6 3 3 0 0 1 0 6z"/></symbol>
  </defs>
</svg>

<main class="canvas">
  <section class="sheet letterhead" aria-label="Letterhead">
    <div class="wordmark"><span class="mark-square"></span>BRENNAN LAW</div>
    <svg class="footer-band" viewBox="0 0 758 80" width="758" height="80" aria-hidden="true">
      <polygon points="0,0 363,0 335,80 0,80" fill="var(--brand-blue)"/>
      <polygon points="420,0 758,0 758,80 391,80" fill="var(--brand-blue)"/>
    </svg>
    <div class="contact left">
      <div class="row"><svg><use href="#icon-phone"/></svg>555-0142-0000</div>
      <div class="row"><svg><use href="#icon-mail"/></svg>info@brennanlaw.com</div>
    </div>
    <div class="contact right">
      <div class="row"><svg><use href="#icon-pin"/></svg><span>48/B, Harbour Lane,<br>Postcode-204518</span></div>
    </div>
  </section>

  <section class="sheet card-front" aria-label="Business card, front">
    <div class="wordmark on-blue"><span class="mark-square"></span>BRENNAN LAW</div>
    <p class="person">Your Name/<span class="role">CEO</span></p>
    <div class="contact left">
      <div class="row"><svg><use href="#icon-phone"/></svg>555-0142-0000</div>
      <div class="row"><svg><use href="#icon-mail"/></svg>info@brennanlaw.com</div>
    </div>
    <div class="contact right">
      <div class="row"><svg><use href="#icon-pin"/></svg><span>48/B, Harbour Lane,<br>Postcode-204518</span></div>
    </div>
  </section>

  <section class="sheet card-back" aria-label="Business card, back">
    <div class="wordmark"><span class="mark-square"></span>BRENNAN LAW</div>
  </section>

  <section class="sheet envelope" aria-label="Envelope">
    <div class="wordmark"><span class="mark-square"></span>BRENNAN LAW</div>
    <svg class="footer-band" viewBox="0 0 676 70" width="676" height="70" aria-hidden="true">
      <polygon points="0,0 327,0 301,70 0,70" fill="var(--brand-blue)"/>
      <polygon points="370,0 676,0 676,70 348,70" fill="var(--brand-blue)"/>
    </svg>
    <div class="contact left">
      <div class="row"><svg><use href="#icon-phone"/></svg>555-0142-0000</div>
      <div class="row"><svg><use href="#icon-mail"/></svg>info@brennanlaw.com</div>
    </div>
    <div class="contact right">
      <div class="row"><svg><use href="#icon-pin"/></svg><span>48/B, Harbour Lane,<br>Postcode-204518</span></div>
    </div>
  </section>
</main>
</body>
</html>
```